Finiding oppertunites in Real Estate 6.15.20

size of ad 7” x 9.6”
1-I like the ad to stand out and attract people's attention.
2-you should be able to see the text of the ad clearly .. see the attachment anything in yellow is instructions.
3-the list of topics should not be the main part of the ad
4-if you decide you want a picture or vector of a person .. (you decide)
then it should be a white male about 25-30 years old wearing a solid white or blue shirt and not long hair.
5-leave 1 inch for footer
see attachment
Good luck

Target Market(s)

potential male students 25-35 years of age

Industry/Entity Type

Education

Requirements
Must have
• will stand out and people would want to see it.
should be able to read the words of ad
Nice to have
• how to make money in real estate on one line

```html
<!DOCTYPE html>
<html lang="en">
<head>
<meta charset="utf-8">
<title>Real Estate Course – Flyer Options</title>
<link rel="stylesheet" href="https://fonts.googleapis.com/css2?family=Bebas+Neue&family=Montserrat:wght@500;600;700;800&display=swap">
<style>
  :root {
    --stage: #bdbdbd;
    --orange: #e3860a;
    --navy: #263f6a;
    --navy-deep: #1f3459;
    --red: #e0161b;
    --paper: #ffffff;
    --paper-shade: #f1f1f1;
    --ink: #2a3f68;
    --label: #2b2b2b;
    --photo-light: #c9dbef;
    --photo-dark: #7f95b5;
  }
  * { margin: 0; padding: 0; box-sizing: border-box; }
  html, body { width: 1200px; height: 792px; overflow: hidden; }
  body { background: var(--stage); position: relative; font-family: "Montserrat", sans-serif; }

  .flyer {
    position: absolute;
    top: 55px;
    width: 482px;
    height: 660px;
    background: linear-gradient(180deg, var(--paper) 70%, var(--paper-shade) 100%);
    overflow: hidden;
  }
  .flyer--a { left: 88px; }
  .flyer--b { left: 655px; }

  .flyer__art { position: absolute; inset: 0; width: 482px; height: 660px; }

  .flyer__title {
    position: absolute;
    left: 0; top: 14px;
    width: 342px;
    text-align: center;
    font-family: "Bebas Neue", sans-serif;
    color: var(--paper);
    font-size: 76px;
    line-height: 56px;
    letter-spacing: -0.5px;
  }
  .flyer__title span { display: block; }
  .flyer__title .course { font-size: 82px; line-height: 58px; }

  .flyer__question {
    position: absolute;
    left: 0; top: 156px;
    width: 342px;
    text-align: center;
    color: var(--paper);
    font-weight: 600;
    font-size: 28px;
    line-height: 35px;
  }

  .flyer__tagline {
    position: absolute;
    left: 23px; top: 244px;
    color: var(--ink);
    font-weight: 700;
    font-size: 19px;
    line-height: 23px;
  }
  .flyer--b .flyer__tagline { top: 240px; }

  .flyer__audience {
    position: absolute;
    left: 22px;
    color: var(--ink);
    font-weight: 500;
    font-size: 12px;
    line-height: 16px;
  }
  .flyer--a .flyer__audience { top: 443px; }
  .flyer--b .flyer__audience { top: 325px; }

  .badge {
    position: absolute;
    width: 104px; height: 104px;
    left: 20px;
  }
  .flyer--a .badge { top: 326px; }
  .flyer--b .badge { top: 376px; }
  .badge svg { position: absolute; inset: 0; }
  .badge__text {
    position: absolute; inset: 0;
    display: flex; flex-direction: column; justify-content: center; align-items: center;
    font-family: "Bebas Neue", sans-serif;
    color: var(--paper);
    font-size: 27px;
    line-height: 23px;
    text-shadow: 0 1px 2px rgba(0,0,0,0.45);
  }

  .facts { position: absolute; left: 132px; width: 210px; }
  .flyer--a .facts { top: 350px; }
  .flyer--b .facts { top: 400px; }
  .fact { display: flex; align-items: center; height: 26px; margin-bottom: 6px; }
  .fact__num {
    width: 34px;
    color: var(--red);
    font-weight: 800;
    font-size: 25px;
    line-height: 22px;
    text-align: center;
    letter-spacing: -1px;
  }
  .fact__num small { display: block; font-size: 9px; line-height: 9px; letter-spacing: 0; font-weight: 700; }
  .fact__label {
    flex: 1;
    height: 26px;
    margin-left: 4px;
    padding-left: 6px;
    border-left: 1px solid #d7c49a;
    background: linear-gradient(90deg, #ececec 0%, #f2f2f2 60%, rgba(255,255,255,0) 100%);
    color: var(--label);
    font-weight: 600;
    font-size: 11px;
    line-height: 11px;
    display: flex; flex-direction: column; justify-content: center;
  }
</style>
</head>
<body>

  <article class="flyer flyer--a">
    <svg class="flyer__art" viewBox="0 0 482 660" aria-hidden="false">
      <defs>
        <linearGradient id="photoA" x1="0" y1="0" x2="0" y2="1">
          <stop offset="0" stop-color="#9c7a62"/>
          <stop offset="0.3" stop-color="var(--photo-light)"/>
          <stop offset="1" stop-color="var(--photo-dark)"/>
        </linearGradient>
      </defs>
      <rect x="0" y="0" width="482" height="145" fill="var(--orange)"/>
      <path d="M316,80 L409,9 L482,62 L482,230 L332,230 L332,90 L321,92 Z" fill="var(--navy)"/>
      <rect x="0" y="145" width="482" height="85" fill="var(--navy)"/>
      <path role="img" aria-label="Photo of a smiling young man in a light blue shirt and dark tie, arms crossed" d="M345,100 L482,100 L482,490 L255,490 L255,232 L345,232 Z" fill="url(#photoA)"/>
      <path d="M0,490 L482,490 L482,496 L232,496 Q222,496 215,505 L210,512 Q206,516 196,516 L0,516 Z" fill="var(--navy)"/>
    </svg>
    <h1 class="flyer__title"><span>Real Estate</span><span class="course">Course</span></h1>
    <p class="flyer__question">How to Make Money<br>In Real Estate?</p>
    <p class="flyer__tagline">INVESTING IN<br>KNOWLEDGE OPENS UP<br>OPPORTUNITIES</p>
    <div class="badge">
      <svg viewBox="-52 -52 104 104" aria-hidden="true"><polygon fill="var(--red)" points="50,0 42.2,8.4 46.2,19.1 35.7,23.9 35.4,35.4 23.9,35.7 19.1,46.2 8.4,42.2 0,50 -8.4,42.2 -19.1,46.2 -23.9,35.7 -35.4,35.4 -35.7,23.9 -46.2,19.1 -42.2,8.4 -50,0 -42.2,-8.4 -46.2,-19.1 -35.7,-23.9 -35.4,-35.4 -23.9,-35.7 -19.1,-46.2 -8.4,-42.2 0,-50 8.4,-42.2 19.1,-46.2 23.9,-35.7 35.4,-35.4 35.7,-23.9 46.2,-19.1 42.2,-8.4"/></svg>
      <div class="badge__text"><span>Remote</span><span>Sessions</span></div>
    </div>
    <div class="facts">
      <div class="fact"><div class="fact__num">12</div><div class="fact__label"><span>SESSION</span><span>COURSE</span></div></div>
      <div class="fact"><div class="fact__num">16<small>JUNE</small></div><div class="fact__label"><span>CLASS</span><span>STARTING</span></div></div>
    </div>
    <p class="flyer__audience">FOR THOSE WHO HAVE STARTED OR<br>WOULD LIKE TO GO INTO REAL ESTATE</p>
  </article>

  <article class="flyer flyer--b">
    <svg class="flyer__art" viewBox="0 0 482 660">
      <defs>
        <linearGradient id="photoB" x1="0" y1="0" x2="0" y2="1">
          <stop offset="0" stop-color="#9c7a62"/>
          <stop offset="0.3" stop-color="var(--photo-light)"/>
          <stop offset="1" stop-color="var(--photo-dark)"/>
        </linearGradient>
      </defs>
      <rect x="0" y="0" width="482" height="145" fill="var(--orange)"/>
      <path d="M316,80 L409,9 L482,62 L482,230 L332,230 L332,90 L321,92 Z" fill="var(--navy)"/>
      <rect x="0" y="145" width="482" height="85" fill="var(--navy)"/>
      <path role="img" aria-label="Photo of a smiling young man in a light blue shirt and dark tie, arms crossed" d="M345,100 L482,100 L482,490 L255,490 L255,232 L345,232 Z" fill="url(#photoB)"/>
      <path d="M0,490 L482,490 L482,496 L232,496 Q222,496 215,505 L210,512 Q206,516 196,516 L0,516 Z" fill="var(--navy)"/>
    </svg>
    <h1 class="flyer__title"><span>Real Estate</span><span class="course">Course</span></h1>
    <p class="flyer__question">How to Make Money<br>In Real Estate?</p>
    <p class="flyer__tagline">INVESTING IN<br>KNOWLEDGE OPENS UP<br>OPPORTUNITIES</p>
    <p class="flyer__audience">FOR THOSE WHO HAVE STARTED OR<br>WOULD LIKE TO GO INTO REAL ESTATE</p>
    <div class="badge">
      <svg viewBox="-52 -52 104 104" aria-hidden="true"><polygon fill="var(--red)" points="50,0 42.2,8.4 46.2,19.1 35.7,23.9 35.4,35.4 23.9,35.7 19.1,46.2 8.4,42.2 0,50 -8.4,42.2 -19.1,46.2 -23.9,35.7 -35.4,35.4 -35.7,23.9 -46.2,19.1 -42.2,8.4 -50,0 -42.2,-8.4 -46.2,-19.1 -35.7,-23.9 -35.4,-35.4 -23.9,-35.7 -19.1,-46.2 -8.4,-42.2 0,-50 8.4,-42.2 19.1,-46.2 23.9,-35.7 35.4,-35.4 35.7,-23.9 46.2,-19.1 42.2,-8.4"/></svg>
      <div class="badge__text"><span>Remote</span><span>Sessions</span></div>
    </div>
    <div class="facts">
      <div class="fact"><div class="fact__num">12</div><div class="fact__label"><span>SESSION</span><span>COURSE</span></div></div>
      <div class="fact"><div class="fact__num">16<small>JUNE</small></div><div class="fact__label"><span>CLASS</span><span>STARTING</span></div></div>
    </div>
  </article>

</body>
</html>
```